Business Card Design

My husband & I have a singing business so just need a card with my husband's photo on it and our current logo. I have attached the logo on the top of a page plus a photo of my husband & our theme colour we would like is a black background with red writing to match our logo. If you can please also put somewhere on the card "Entertainment for any occasion inc. Pubs, Clubs, Birthday Parties or Weddings". The photo is on the poster attached if you are able to copy it please.

Industry/Entity Type

Business

Contact Information for Business Card

Rocco & Jen Farley
Mobile: 0498 362 514
Email: janice.brook@mailnest.example

```html
<!DOCTYPE html>
<html lang="en">
<head>
<meta charset="utf-8">
<title>Encore Lane Entertainment – Business Card</title>
<link rel="stylesheet" href="https://fonts.googleapis.com/css2?family=Questrial&display=swap">
<style>
  :root {
    --page-bg: #d9d4cf;
    --card-black: #0b0b0c;
    --card-charcoal: #2a2a2c;
    --silver-light: #ecebe8;
    --silver-mid: #c9c6c1;
    --silver-dark: #9d9a95;
    --brand-red: #c8282a;
    --tag-red: #e0403a;
    --tag-cream: #e9e2d6;
    --ink-dark: #2b2b2b;
    --ink-soft: #4a4a4a;
    --photo-warm: #8a4a3c;
    --photo-deep: #2a1a16;
  }
  * { box-sizing: border-box; margin: 0; padding: 0; }
  html, body {
    width: 1200px;
    height: 970px;
    overflow: hidden;
    background: var(--page-bg);
    font-family: "Questrial", "Century Gothic", sans-serif;
  }
  .business-card {
    position: absolute;
    left: 100px;
    top: 200px;
    width: 1000px;
    height: 570px;
    border-radius: 26px;
    overflow: hidden;
    background: var(--card-black);
    box-shadow: 0 12px 40px rgba(0,0,0,0.3);
  }
  .card-shapes {
    position: absolute;
    inset: 0;
  }
  .brand-mark {
    position: absolute;
    left: 140px;
    top: 108px;
    display: flex;
    align-items: center;
    gap: 16px;
  }
  .brand-dot {
    width: 30px;
    height: 30px;
    border-radius: 50%;
    background: var(--silver-mid);
  }
  .brand-name {
    color: var(--brand-red);
    font-size: 40px;
    line-height: 1;
    font-weight: 400;
    white-space: nowrap;
  }
  .tagline {
    position: absolute;
    left: 30px;
    width: 700px;
    top: 222px;
    text-align: center;
    font-size: 27px;
    line-height: 1.3;
  }
  .tagline-lead { color: var(--tag-red); }
  .tagline-venues { color: var(--tag-cream); }
  .contact-name {
    position: absolute;
    left: 45px;
    top: 400px;
    font-size: 43px;
    font-weight: 400;
    color: var(--ink-dark);
    letter-spacing: 0.5px;
  }
  .contact-lines {
    position: absolute;
    left: 45px;
    top: 460px;
    display: flex;
    gap: 30px;
    font-size: 26px;
    color: var(--ink-soft);
  }
  .contact-item {
    display: flex;
    align-items: center;
    gap: 12px;
  }
  .contact-icon { width: 28px; height: 22px; }
  .portrait-area {
    position: absolute;
    left: 696px;
    top: 186px;
    width: 304px;
    height: 384px;
    background: radial-gradient(ellipse at 45% 45%, var(--photo-warm) 0%, #5a2f26 45%, var(--photo-deep) 100%);
  }
</style>
</head>
<body>
  <main class="business-card">
    <svg class="card-shapes" viewBox="0 0 1000 570" width="1000" height="570" aria-hidden="true">
      <defs>
        <linearGradient id="topBlack" x1="0" y1="0" x2="1" y2="0">
          <stop offset="0" stop-color="#161617"/>
          <stop offset="0.45" stop-color="#050505"/>
          <stop offset="1" stop-color="#2a2a2c"/>
        </linearGradient>
        <linearGradient id="silverBand" x1="0" y1="0" x2="1" y2="0">
          <stop offset="0" stop-color="#a9a6a1"/>
          <stop offset="0.3" stop-color="#ecebe8"/>
          <stop offset="0.55" stop-color="#d3ccc8"/>
          <stop offset="0.8" stop-color="#ecebe8"/>
          <stop offset="1" stop-color="#b8b5b0"/>
        </linearGradient>
      </defs>
      <rect width="1000" height="570" fill="url(#topBlack)"/>
      <path d="M0 320 C 250 350, 600 350, 1000 318 L1000 540 C 650 520, 300 515, 0 530 Z" fill="url(#silverBand)"/>
      <path d="M0 530 C 300 515, 650 520, 1000 540 L1000 570 L0 570 Z" fill="#0b0b0c"/>
    </svg>

    <div class="brand-mark">
      <span class="brand-dot"></span>
      <span class="brand-name">Encore Lane Entertainment</span>
    </div>

    <p class="tagline">
      <span class="tagline-lead">Entertainment for any occasion inc</span><br>
      <span class="tagline-venues">Pubs, Clubs, Birthday Parties or Weddings</span>
    </p>

    <h1 class="contact-name">Rocco &amp; Jen Farley</h1>
    <div class="contact-lines">
      <span class="contact-item">
        <svg class="contact-icon" viewBox="0 0 28 22" aria-hidden="true">
          <path d="M2 8 C2 3, 26 3, 26 8 L22 10 L19 7 L9 7 L6 10 Z" fill="var(--brand-red)"/>
          <rect x="5" y="11" width="18" height="10" rx="2" fill="var(--brand-red)"/>
        </svg>
        0498 362 514
      </span>
      <span class="contact-item">
        <svg class="contact-icon" viewBox="0 0 28 22" aria-hidden="true">
          <rect x="2" y="3" width="24" height="16" rx="1" fill="var(--brand-red)"/>
          <path d="M2 4 L14 13 L26 4" fill="none" stroke="#f1d6d4" stroke-width="1.6"/>
        </svg>
        janice.brook@mailnest.example
      </span>
    </div>

    <div class="portrait-area" role="img" aria-label="Photo of the male singer, head and shoulders"></div>
  </main>
</body>
</html>
```